Brivane Communications - veteran and exclusive boutique copywriting agency

PROJECT NEEDS:
1. Website design - full homepage design and inner page top banner design
2. Logo design
* Please see attached Briefs (Word Docs) for descriptions of what is needed for 1 and 2 above.
ABOUT THE CLIENT:
Brivane Communications is a veteran and exclusive boutique copywriting agency run by Martin Olafsky. Martin is an award-winning published novelist and an accomplished executive ghostwriter with articles regularly published prominent technology publications like Pulsar, ByteHarbor, CapitalDrift, and more. For nearly three decades, Martin has focused solely on the technology sector - serving clients in Israel, Europe and the US.

Target Market(s)

hi-tech companies run by serious, confident professionals.

Industry/Entity Type

Business

Number of Pages Required

2 page

Font styles to use
Sans Serif
Other font styles liked:
• font should be modern

Colors
0054AA
0677BA
7BADD7
CADEEF
E8F1F8
F0912C
F2A743
F7CA91
FBE8D2
FDF5EE

Requirements
Must have
• psd files for logo, homepage design, and inner page top banner design
Nice to have
• Please see attached Website and Logo Design Briefs (Word Docs)
Should not have

```html
<!DOCTYPE html>
<html lang="en">
<head>
<meta charset="utf-8">
<title>Brivane Communications</title>
<link href="https://fonts.googleapis.com/css2?family=Poppins:wght@400;500;600;700&display=swap" rel="stylesheet">
<style>
:root{
  --blue:#0677BA;
  --blue-dark:#0054AA;
  --orange:#F0912C;
  --dark:#161a22;
  --gray-bg:#f1f1f1;
  --text:#2b2b2b;
  --muted:#8a8a8a;
  --white:#ffffff;
  --star:#F2A743;
}
*{box-sizing:border-box;margin:0;padding:0}
html,body{width:1200px;height:3539px;overflow:hidden}
body{font-family:'Poppins',sans-serif;color:var(--text);background:var(--white);position:relative}
.abs{position:absolute}
section,header,footer{position:absolute;left:0;width:1200px}

/* header */
.site-header{top:0;height:103px;background:var(--white)}
.brand{left:85px;top:30px;color:var(--blue);font-weight:600;line-height:1}
.brand .brand-name{font-size:34px;letter-spacing:1px}
.brand .brand-sub{font-size:9.5px;letter-spacing:1.2px;margin-top:4px}
.main-nav{left:503px;top:46px;display:flex;gap:29px;font-size:14px;color:#444}
.social{top:41px;left:987px;display:flex;gap:3px}
.social span{width:30px;height:30px;border-radius:50%;background:var(--blue);color:var(--white);font-size:9px;font-weight:600;display:flex;align-items:center;justify-content:center}

/* hero */
.hero{top:103px;height:577px;background:var(--dark);overflow:hidden}
.hero-photo{left:729px;top:0;width:471px;height:577px;background:radial-gradient(ellipse at 55% 45%,#5c7fb0 0%,#2f3f5a 35%,#1a1f2a 70%,var(--dark) 100%)}
.hero h1{left:158px;top:152px;font-size:41px;font-weight:700;color:var(--white);letter-spacing:.3px}
.hero h1 em{font-style:normal;color:var(--orange)}
.hero p{left:158px;top:215px;width:470px;font-size:16.5px;line-height:26px;color:var(--white)}
.btn{background:var(--orange);color:var(--white);font-weight:500;display:flex;align-items:center;justify-content:center}
.hero .btn{left:158px;top:292px;width:162px;height:52px;font-size:16px}

/* clients */
.clients{top:680px;height:319px}
.section-title{width:100%;text-align:center;color:var(--orange);font-weight:700;font-size:30px;letter-spacing:.3px}
.clients .section-title{top:83px}
.arrow{width:24px;height:38px}
.client-row{left:155px;top:196px;width:890px;display:flex;justify-content:space-between;align-items:center}
.client{display:flex;align-items:center;gap:8px;font-size:28px;font-weight:500;color:#2f2f3a}
.client i{display:inline-block;width:16px;height:16px;border-radius:50%;background:var(--blue)}

/* services */
.services{top:999px;height:696px;background:var(--gray-bg)}
.services .section-title{top:90px}
.card{top:184px;width:326px;height:402px;background:var(--white);text-align:center}
.card-img{width:326px;height:179px}
.card h3{margin-top:33px;font-size:14.5px;font-weight:500;color:var(--blue);letter-spacing:.3px}
.card p{margin:14px auto 0;width:300px;font-size:13px;line-height:21px;color:var(--muted)}
.card .btn{position:absolute;left:101px;top:326px;width:124px;height:41px;font-size:13px}

/* why */
.why{top:1695px;height:676px}
.why h2{left:85px;top:96px;font-size:30px;font-weight:700;color:var(--orange)}
.why p{left:85px;top:154px;width:540px;font-size:15px;line-height:26px}
.why ul{left:141px;top:280px;list-style:none;font-size:15.5px;line-height:31px}
.why li{position:relative;padding-left:13px}
.why li:before{content:"";position:absolute;left:-4px;top:11px;width:10px;height:10px;border-radius:50%;background:var(--orange)}
.why-photo{left:698px;top:78px;width:417px;height:543px;background:radial-gradient(ellipse at 50% 45%,#6d8fbf 0%,#3a4d6c 40%,#1c222c 80%)}

/* testimonials */
.testimonials{top:2371px;height:653px;background:var(--gray-bg)}
.testimonials .section-title{top:80px}
.bubble{background:var(--white);border-radius:22px;width:332px;height:217px}
.bubble .q{position:absolute;font-size:26px;color:#555;font-weight:500;line-height:1}
.bubble p{position:absolute;left:42px;width:272px;font-size:13.5px;line-height:21px;color:#666}
.avatar{width:82px;height:82px;border-radius:50%;background:radial-gradient(circle at 50% 40%,#cfd6df 0%,#7a8596 55%,#39414f 100%)}
.person{font-size:13px;font-weight:600;color:var(--text)}
.person small{display:block;font-size:9px;font-weight:400;color:#777;margin-top:2px}
.person .stars{color:var(--star);font-size:11px;letter-spacing:1px;margin-top:2px}

/* newsletter */
.newsletter{top:3024px;height:194px}
.newsletter h2{left:85px;top:80px;font-size:32px;font-weight:400}
.nl-input{left:393px;top:72px;width:436px;height:67px;background:var(--blue);color:var(--white);font-size:15px;padding-left:15px;display:flex;align-items:center}
.nl-btn{left:848px;top:72px;width:267px;height:67px;font-size:15px}

/* footer */
.site-footer{top:3218px;height:321px;background:var(--blue);color:var(--white)}
.site-footer .brand{left:301px;top:72px;color:var(--white);text-align:center}
.site-footer .brand .brand-name{font-size:42px}
.site-footer .brand .brand-sub{font-size:13px}
.foot-social{left:301px;top:177px;display:flex;gap:7px}
.foot-social span{width:36px;height:36px;border-radius:50%;border:1.5px solid var(--white);font-size:10px;display:flex;align-items:center;justify-content:center}
.foot-col h4{font-size:13px;font-weight:600;margin-bottom:14px}
.quick{left:569px;top:67px}
.quick a{display:block;color:var(--white);text-decoration:none;font-size:12px;line-height:20.6px}
.contact{left:729px;top:66px}
.contact-item{display:flex;gap:8px;font-size:12px;line-height:15px;margin-bottom:20px}
.contact-item svg{flex:none;margin-top:1px}
.foot-rule{left:85px;top:264px;width:1030px;height:1px;background:rgba(255,255,255,.7)}
.copyright{top:286px;width:1200px;text-align:center;font-size:12px}
</style>
</head>
<body>

<header class="site-header">
  <div class="abs brand"><div class="brand-name">Brivane</div><div class="brand-sub">COMMUNICATIONS</div></div>
  <nav class="abs main-nav"><span>About</span><span>Services</span><span>Industries</span><span>Portfolio</span><span>Clients</span><span>Contact</span></nav>
  <div class="abs social"><span>Vo</span><span>Pi</span><span>Lu</span><span>Re</span></div>
</header>

<section class="hero">
  <div class="abs hero-photo" role="img" aria-label="Portrait of Martin Olafsky in a light blue shirt against a dark backdrop"></div>
  <h1 class="abs">YOUR VOICE, <em>MY WORDS.</em></h1>
  <p class="abs">Copywriting and executive ghostwriting that speaks for your vision and your technology.</p>
  <div class="abs btn">Read More</div>
</section>

<section class="clients">
  <h2 class="abs section-title">OUR CLIENTS</h2>
  <svg class="abs arrow" style="left:85px;top:201px" viewBox="0 0 24 38"><path d="M19 4 5 19l14 15" fill="none" stroke="#0677BA" stroke-width="5"/></svg>
  <div class="abs client-row">
    <span class="client"><i></i>Ardeline</span>
    <span class="client">Quorvo</span>
    <span class="client">Tessaro</span>
    <span class="client">Kelvix</span>
    <span class="client">Mirolen</span>
  </div>
  <svg class="abs arrow" style="left:1088px;top:201px" viewBox="0 0 24 38"><path d="M5 4l14 15L5 34" fill="none" stroke="#0677BA" stroke-width="5"/></svg>
</section>

<section class="services">
  <h2 class="abs section-title">WHAT I DO</h2>
  <article class="abs card" style="left:85px">
    <div class="card-img" role="img" aria-label="Child in a hat looking through a telescope" style="background:linear-gradient(160deg,#e9e3d4,#a9b489 60%,#5f8a3e)"></div>
    <h3>MESSAGING</h3>
    <p>Lorem ipsum dolor sit amet, consectetur adipiscing elit, sed do eiusmod tempor incididunt ut labore et dolore magna</p>
    <div class="btn">Read More</div>
  </article>
  <article class="abs card" style="left:437px">
    <div class="card-img" role="img" aria-label="Child writing on a chalkboard" style="background:linear-gradient(160deg,#55584f,#3d403a 60%,#6a6d43)"></div>
    <h3>COLLATERAL</h3>
    <p>Lorem ipsum dolor sit amet, consectetur adipiscing elit, sed do eiusmod tempor incididunt ut labore et dolore magna</p>
    <div class="btn">Read More</div>
  </article>
  <article class="abs card" style="left:789px">
    <div class="card-img" role="img" aria-label="Child fishing by the water" style="background:linear-gradient(160deg,#d7e3ea,#a9bdc8 55%,#c9b59a)"></div>
    <h3>CONTENT MARKETING</h3>
    <p>Lorem ipsum dolor sit amet, consectetur adipiscing elit, sed do eiusmod tempor incididunt ut labore et dolore magna</p>
    <div class="btn">Read More</div>
  </article>
</section>

<section class="why">
  <h2 class="abs">WHY CHOOSE ME</h2>
  <p class="abs">Since 2001, Brivane Communications has had the opportunity to create collateral and content for tens of companies across a wide range of industries. Following is a small selection of recent projects:</p>
  <ul class="abs">
    <li>Contributed Content</li>
    <li>Blog Content</li>
    <li>White Papers &amp; E-Books</li>
    <li>Case Studies</li>
    <li>Web Site Content</li>
    <li>Video - Concept and Script</li>
    <li>Press Releases</li>
    <li>Collateral (brochures, datasheets and more)</li>
  </ul>
  <div class="abs why-photo" role="img" aria-label="Portrait of Martin Olafsky standing with hands in pockets"></div>
</section>

<section class="testimonials">
  <h2 class="abs section-title">WHAT THEY’RE SAYING</h2>
  <svg class="abs arrow" style="left:85px;top:355px" viewBox="0 0 24 38"><path d="M19 4 5 19l14 15" fill="none" stroke="#0677BA" stroke-width="5"/></svg>
  <svg class="abs arrow" style="left:1090px;top:355px" viewBox="0 0 24 38"><path d="M5 4l14 15L5 34" fill="none" stroke="#0677BA" stroke-width="5"/></svg>

  <div class="abs bubble" style="left:223px;top:172px">
    <span class="q" style="left:27px;top:42px">“</span>
    <p style="top:66px">Martin has been a pleasure to work with. He provides great ideas, thorough work in a great turn around time.</p>
    <span class="q" style="left:278px;top:118px">”</span>
  </div>
  <svg class="abs" style="left:335px;top:385px" width="80" height="65" viewBox="0 0 80 65"><path d="M20 0h60L0 65z" fill="#fff"/></svg>
  <div class="abs avatar" style="left:246px;top:451px" role="img" aria-label="Headshot of Noa Feldtree"></div>
  <div class="abs person" style="left:344px;top:472px">Noa Feldtree<small>CMO, Kestrel Media</small><div class="stars">★★★★★</div></div>

  <div class="abs avatar" style="left:682px;top:178px" role="img" aria-label="Headshot of Dalia Remond"></div>
  <div class="abs person" style="left:780px;top:193px">Dalia Remond<small>CMO, Halvex</small><div class="stars">★★★★★</div></div>
  <svg class="abs" style="left:775px;top:255px" width="80" height="62" viewBox="0 0 80 62"><path d="M0 0l80 62H25z" fill="#fff"/></svg>
  <div class="abs bubble" style="left:661px;top:315px">
    <span class="q" style="left:27px;top:50px">“</span>
    <p style="top:76px">“Martin has rich experience in the security arena, and a unique ability to get up speed quickly on material.</p>
    <span class="q" style="left:278px;top:128px">”</span>
  </div>
</section>

<section class="newsletter">
  <h2 class="abs">Sign For Newsletter</h2>
  <div class="abs nl-input">Enter Email Here</div>
  <div class="abs btn nl-btn">SUBCRIBE</div>
</section>

<footer class="site-footer">
  <div class="abs brand"><div class="brand-name">Brivane</div><div class="brand-sub">COMMUNICATIONS</div></div>
  <div class="abs foot-social"><span>Vo</span><span>Pi</span><span>Lu</span><span>Ti</span></div>
  <div class="abs foot-col quick">
    <h4>QUICK LINKS</h4>
    <a>About</a><a>Services</a><a>Industries</a><a>Portfolio</a><a>Clients</a><a>Contact</a>
  </div>
  <div class="abs foot-col contact">
    <h4>CONTACT US</h4>
    <div class="contact-item"><svg width="13" height="16" viewBox="0 0 13 16"><path d="M6.5 0A6 6 0 0 0 .5 6c0 4.5 6 10 6 10s6-5.5 6-10a6 6 0 0 0-6-6zm0 8.5a2.5 2.5 0 1 1 0-5 2.5 2.5 0 0 1 0 5z" fill="#fff"/></svg><span>P.O. Box 1187<br>Ramot Tal, Israel 40215</span></div>
    <div class="contact-item"><svg width="14" height="14" viewBox="0 0 14 14"><path d="M3 0l3 3.5-1.7 2a8 8 0 0 0 3.7 3.7l2-1.7L14 11l-2 3C5.5 14 0 8.5 0 2z" fill="#fff"/></svg><span>+972-50-000-1842</span></div>
    <div class="contact-item"><svg width="16" height="12" viewBox="0 0 16 12"><rect x=".75" y=".75" width="14.5" height="10.5" fill="none" stroke="#fff" stroke-width="1.5"/><path d="M1 1l7 6 7-6" fill="none" stroke="#fff" stroke-width="1.5"/></svg><span>hello@brivane.co</span></div>
  </div>
  <div class="abs foot-rule"></div>
  <div class="abs copyright">Copyright © 2022 Brivane Communications</div>
</footer>

</body>
</html>
```